Marwick Law Letterhead

We need a new letterhead design for a Law Firm. The address for the law firm is 4175 Calloway Avenue, Suite 200, Houston, Texas 77046. Phone Number: 832-614-2093; Fax Number: 832-307-1546. The logo is uploaded to the project.

```html
<!DOCTYPE html>
<html lang="en">
<head>
<meta charset="utf-8">
<title>Marwick Law Letterhead</title>
<link href="https://fonts.googleapis.com/css2?family=Montserrat:wght@400;500;600&family=Tinos&display=swap" rel="stylesheet">
<style>
  :root{
    --backdrop:#a9aaad;
    --paper:#ffffff;
    --navy:#1b3263;
    --navy-dark:#142850;
    --red:#b81d27;
    --ink:#3a3a3a;
    --muted:#8a8a8a;
    --signature:#eceef2;
  }
  *{margin:0;padding:0;box-sizing:border-box}
  html,body{width:1200px;height:1200px;overflow:hidden;background:var(--backdrop)}
  .letterhead{
    position:absolute;left:226px;top:56px;width:748px;height:1056px;
    background:var(--paper);font-family:"Montserrat",sans-serif;color:var(--muted);
    overflow:hidden;
  }
  .brand{position:absolute;left:81px;top:56px;display:flex;align-items:center;gap:10px}
  .brand-mark{width:14px;height:14px;border-radius:50%;background:var(--navy)}
  .brand-name{font-weight:600;font-size:26px;color:var(--navy);letter-spacing:.5px}
  .recipient{position:absolute;left:76px;top:236px}
  .recipient-label{font-size:13px;color:var(--ink);letter-spacing:2px;font-weight:500}
  .recipient-name{font-size:13px;color:var(--red);margin-top:8px;font-weight:500}
  .recipient-lines{margin-top:6px;font-size:10.5px;line-height:16.4px}
  .date{position:absolute;right:76px;top:236px;font-size:10.5px;color:var(--ink)}
  .body-copy{position:absolute;left:76px;top:378px;width:597px;font-size:10.8px;line-height:13.2px;text-align:justify}
  .body-copy p{margin-bottom:13.2px}
  .signature{position:absolute;left:76px;top:744px;width:130px;height:32px;background:var(--signature);border-radius:3px}
  .signer{position:absolute;left:75px;top:786px}
  .signer-name{font-size:12px;color:var(--ink);font-weight:500}
  .signer-title{font-size:9.5px;margin-top:3px}
  .footer-rule{position:absolute;left:0;top:926px;width:748px;height:5px;background:var(--red)}
  .footer-band{position:absolute;left:0;top:936px;width:748px;height:120px;background:linear-gradient(90deg,var(--navy),var(--navy-dark))}
  .contact{position:absolute;left:41px;top:966px;font-family:"Tinos",serif;font-size:12px;color:#fff;line-height:15.5px}
  .contact-row{display:flex;align-items:center;gap:6px}
  .contact-address{margin-top:5px}
  .contact svg{width:10px;height:10px;fill:#fff;flex:none}
</style>
</head>
<body>
<main class="letterhead">
  <header class="brand">
    <span class="brand-mark"></span>
    <span class="brand-name">Marwick Law</span>
  </header>

  <section class="recipient">
    <div class="recipient-label">TO</div>
    <div class="recipient-name">Daniel Reyland</div>
    <div class="recipient-lines">
      Human Resources<br>
      Northfield Systems Inc.<br>
      2240-B Linden Crest, Harmon<br>
      K41 USA
    </div>
  </section>
  <div class="date">Friday, 01/01/2018</div>

  <section class="body-copy">
    <p>Lorem ipsum dolor sit amet, consectetuer adipiscing elit, sed diam nonmmy nibh euismod tincidunt ut laoreet dolore magna aliquam erat volutpat. Ut wisi enim ad minim veniam, quis nostrud exerci tationmcorper suscipit lobortis nisl ut aliquip ex ea commodo consequat. Duis autem vel eum iriure dolor in hendrerit in vulputate velit esse molestie consequat, vel illum dolore eu feugiat nulla facilisis at vero eros et accumsan et iusto odio dignissim qui blandit praesent luptatum zzril delenit augue duis dolore te feugait nulla facilisi.</p>
    <p>Nam liber tempor cum soluta nobis eleifend option congue nihil imprdiet doming id quod mazim placerat facer possim assum. Typi non habent claritatem insitam;</p>
    <p>Est usus legentis in iis qui facit eorum claritatem.</p>
    <p>Investigationes demonstraverunt lectores legere me lius quod ii legunt saepius. Claritas est etiam processus dynamicus, qui sequitur mutationem consuetudium lectorum. Mirum est notare quam littera gothica, quam nunc putamus parum claram, anteposuerit litterarum formas humanitatis per seacula quarta decima et quinta decima. Eodem modo typi, qui nunc nobis videntur parum clari, fiant sollemnes in futurum.</p>
    <p>consectetuer adipiscing elit, sed diam nonummy nibh euismod tincidunt ut laoreet dolore magna aliquam erat volutpat. Ut wisi enim ad minim veniam, quis nostrud exerci tation ullamcorper suscipit lobortis nisl ut aliquip ex ea commodo consequat. Duis autem vel eum iriure dolor in hendrerit in vulputate velit esse molestie consequat, vel illum dolore eu feugiat nulla facilisis at vero eros et accumsan et iusto odio dignissim qui blandit praesent luptatum zzril delenit augue duis dolore te feugait nulla facilisi.</p>
    <p>Nam liber tempor cum soluta nobis eleifend option congue nihil imperdiet .</p>
  </section>

  <div class="signature" role="img" aria-label="Handwritten signature of Peter Hollins"></div>
  <div class="signer">
    <div class="signer-name">Peter Hollins</div>
    <div class="signer-title">Managing Director</div>
  </div>

  <div class="footer-rule"></div>
  <div class="footer-band"></div>

  <footer class="contact">
    <div class="contact-row">
      <svg viewBox="0 0 24 24"><path d="M6.6 10.8a15.1 15.1 0 0 0 6.6 6.6l2.2-2.2a1 1 0 0 1 1-.25 11.4 11.4 0 0 0 3.6.57 1 1 0 0 1 1 1V20a1 1 0 0 1-1 1A17 17 0 0 1 3 4a1 1 0 0 1 1-1h3.5a1 1 0 0 1 1 1c0 1.25.2 2.45.57 3.6a1 1 0 0 1-.25 1z"/></svg>
      832-614-2093
    </div>
    <div class="contact-row">
      <svg viewBox="0 0 24 24"><path d="M7 2h10v5H7zM4 8h16a2 2 0 0 1 2 2v8h-4v4H6v-4H2v-8a2 2 0 0 1 2-2zm4 9v3h8v-3z"/></svg>
      832-307-1546
    </div>
    <div class="contact-address">
      4175 Calloway Avenue<br>
      Suite 200, Houston, Texas 77046
    </div>
  </footer>
</main>
</body>
</html>
```